business card design

i would like business cards designed. My business provides trade qualified personnel to the mining industry to work on heavy mobile equipment.
please put a excavator(digger) in the background in one design and have one design without so i can compare the difference.
also add info:
my logo(attached) and "mobile equipment repair and maintenance"
name: Derek Holloway
address: 57 Tarrowby RD Brayfield Dunmore DK.
mobile: 0438120957
email: derek@ironvalemx.com

```html
<!DOCTYPE html>
<html lang="en">
<head>
<meta charset="utf-8">
<title>Ironvale Maintenance Services – Business Card</title>
<link rel="stylesheet" href="https://fonts.googleapis.com/css2?family=Lato:wght@400;700;900&display=swap">
<style>
  :root {
    --page-bg: #f1f2f4;
    --card-light: #e4e5e7;
    --card-panel: #dedfe0;
    --navy: #0c2140;
    --brand-blue: #4a77c0;
    --stripe-grey: #a9aab5;
    --stripe-light: #e4e5e7;
    --rule-grey: #a6a7b3;
    --text-light: #eceef2;
  }
  * { margin: 0; padding: 0; box-sizing: border-box; }
  html, body {
    width: 1200px; height: 1000px; overflow: hidden;
    background: var(--page-bg);
    font-family: "Lato", Arial, sans-serif;
  }
  .card {
    position: absolute; left: 312px;
    width: 576px; height: 329px; overflow: hidden;
    box-shadow: 6px 8px 14px rgba(0,0,0,0.18);
  }
  .card--front { top: 133px; background: var(--card-light); }
  .card--back { top: 538px; background: var(--navy); }

  .front__panel {
    position: absolute; left: 297px; top: 0; right: 0; bottom: 0;
    background: var(--card-panel);
  }
  .front__accent { position: absolute; left: 20px; top: 0; }
  .front__divider { position: absolute; left: 280px; top: 168px; }
  .holder-name {
    position: absolute; left: 52px; top: 55px;
    font-size: 31px; font-weight: 700; color: var(--navy);
    letter-spacing: -0.3px;
  }
  .brand { position: absolute; text-align: center; text-transform: uppercase; }
  .brand__name { font-weight: 900; line-height: 1; }
  .brand__line { color: var(--brand-blue); font-weight: 700; line-height: 1; }
  .brand--front { left: 38px; top: 219px; width: 196px; }
  .brand--front .brand__name { font-size: 27px; letter-spacing: 4px; color: var(--navy); }
  .brand--front .brand__line { font-size: 7.6px; letter-spacing: 1px; margin-top: 4px; }
  .brand--back { left: 0; right: 0; top: 138px; }
  .brand--back .brand__name { font-size: 44px; letter-spacing: 7px; color: var(--text-light); }
  .brand--back .brand__line { font-size: 12px; letter-spacing: 1.8px; margin-top: 6px; }

  .contact { position: absolute; left: 323px; color: var(--navy); font-size: 16px; line-height: 19px; }
  .contact__row { display: flex; align-items: center; gap: 14px; }
  .contact__row + .contact__row { margin-top: 7px; }
  .contact__row--address { align-items: flex-start; }
  .contact__row--address svg { margin-top: 1px; }
  .contact--direct { top: 177px; }
  .contact--place { top: 261px; }
  .contact__rule {
    position: absolute; left: 324px; top: 252px;
    width: 185px; height: 2px; background: var(--rule-grey);
  }

  .tagline {
    position: absolute; left: 0; right: 0; top: 244px;
    text-align: center; color: var(--text-light); font-size: 16px;
  }
  .hazard-band { position: absolute; left: 0; top: 291px; }
</style>
</head>
<body>

<section class="card card--front" aria-label="Business card front">
  <div class="front__panel"></div>

  <svg class="front__accent" width="18" height="84" viewBox="0 0 18 84" aria-hidden="true">
    <g fill="var(--brand-blue)">
      <polygon points="0,0 10,0 17,6 17,25 0,14"/>
      <polygon points="0,24 17,35 17,54 0,43"/>
      <polygon points="0,52 17,63 17,82 0,71"/>
    </g>
  </svg>

  <h1 class="holder-name">DEREK HOLLOWAY</h1>

  <div class="brand brand--front">
    <div class="brand__name">Ironvale</div>
    <div class="brand__line">Maintenance Services Pty Ltd</div>
  </div>

  <svg class="front__divider" width="17" height="161" viewBox="0 0 17 161" aria-hidden="true">
    <g fill="var(--stripe-grey)">
      <polygon points="0,0 17,11 17,30 0,19"/>
      <polygon points="0,27 17,38 17,57 0,46"/>
      <polygon points="0,55 17,66 17,85 0,74"/>
      <polygon points="0,83 17,94 17,113 0,102"/>
      <polygon points="0,111 17,122 17,141 0,130"/>
      <polygon points="0,139 17,150 17,161 0,161"/>
    </g>
  </svg>

  <div class="contact contact--direct">
    <div class="contact__row">
      <svg width="20" height="20" viewBox="0 0 20 20" aria-hidden="true">
        <circle cx="10" cy="10" r="10" fill="var(--navy)"/>
        <path d="M6.4 5.2l2 2.3-1 1.3c.7 1.6 1.9 2.8 3.4 3.5l1.3-1 2.3 2-1.1 1.6c-3.9-.4-7.3-3.8-7.7-7.7z" fill="var(--card-panel)"/>
      </svg>
      <span>0438 120 957</span>
    </div>
    <div class="contact__row">
      <svg width="20" height="20" viewBox="0 0 20 20" aria-hidden="true">
        <circle cx="10" cy="10" r="10" fill="var(--navy)"/>
        <path d="M5 8.5l5-3 5 3v5.5H5z" fill="var(--card-panel)"/>
        <path d="M5 8.5l5 3 5-3" fill="none" stroke="var(--navy)" stroke-width="1.2"/>
      </svg>
      <span>derek@ironvalemx.com</span>
    </div>
  </div>

  <div class="contact__rule"></div>

  <div class="contact contact--place">
    <div class="contact__row contact__row--address">
      <svg width="20" height="20" viewBox="0 0 20 20" aria-hidden="true">
        <circle cx="10" cy="10" r="10" fill="var(--navy)"/>
        <path d="M10 4.5a3.8 3.8 0 0 0-3.8 3.8c0 2.8 3.8 7 3.8 7s3.8-4.2 3.8-7A3.8 3.8 0 0 0 10 4.5z" fill="var(--card-panel)"/>
        <circle cx="10" cy="8.3" r="1.4" fill="var(--navy)"/>
      </svg>
      <span>57 Tarrowby RD<br>Brayfield Dunmore DK.</span>
    </div>
  </div>
</section>

<section class="card card--back" aria-label="Business card back">
  <div class="brand brand--back">
    <div class="brand__name">Ironvale</div>
    <div class="brand__line">Maintenance Services Pty Ltd</div>
  </div>
  <p class="tagline">Mobile equipment repair and maintenance</p>
  <svg class="hazard-band" width="576" height="17" viewBox="0 0 576 17" aria-hidden="true">
    <defs>
      <pattern id="hazard" width="28.5" height="17" patternUnits="userSpaceOnUse">
        <polygon points="10,0 28.5,0 19,17 0.5,17" fill="var(--stripe-light)"/>
      </pattern>
    </defs>
    <rect width="576" height="17" fill="url(#hazard)"/>
  </svg>
</section>

</body>
</html>
```